Banner ad to encourage people to complete a survey

This is a banner ad which will be posted on www.velorin.org. The goal of the add is to encourage people to click on it and take the survey.
File Format: Standard .jpg image (no Flash)
Ad dimension (Pixels): 300w x 250d
Max File Size: 24k
- Use a border to differentiate the banner from page content (page background is white)
- No transparent backgrounds
Ad Message: "Speech-Language Pathologist Survey"
Additional text: "Please take two minutes to complete a survey on the future of work patterns for Speech-Language Pathologists and enter a draw to win an Tabrix"
Target Market(s)
The respondents are professional and well educated and the ad/colour scheme should reflect this.
Colors
Designer to choose colors to be used in the design.
Look and feel

```html
<!DOCTYPE html>
<html lang="en">
<head>
<meta charset="utf-8">
<title>Speech-Language Pathologist Survey</title>
<link rel="stylesheet" href="https://fonts.googleapis.com/css2?family=Lato:wght@400;700;900&display=swap">
<style>
  :root {
    --navy: #1b4460;
    --navy-text: #1d3f68;
    --red: #d33b36;
    --button-red: #d8413b;
    --white: #ffffff;
    --photo-light: #e9ebe8;
    --photo-mid: #b9bcb6;
    --photo-teal: #2f6f73;
    --photo-warm: #c9a27c;
  }
  html, body {
    margin: 0;
    padding: 0;
    overflow: hidden;
    background: var(--white);
  }
  .banner {
    position: relative;
    width: 1200px;
    height: 1001px;
    overflow: hidden;
    background: var(--navy);
    font-family: "Lato", Arial, sans-serif;
  }
  .banner-shapes {
    position: absolute;
    inset: 0;
    width: 1200px;
    height: 1001px;
  }
  .brand-name {
    position: absolute;
    left: 37px;
    top: 18px;
    margin: 0;
    font-weight: 700;
    font-size: 40px;
    line-height: 48px;
    color: var(--white);
  }
  .headline {
    position: absolute;
    left: 22px;
    top: 658px;
    margin: 0;
    font-size: 51px;
    line-height: 60px;
    font-weight: 400;
    color: var(--navy-text);
    white-space: nowrap;
    letter-spacing: 0.3px;
  }
  .headline-accent {
    font-weight: 700;
    color: var(--red);
  }
  .body-copy {
    position: absolute;
    left: 68px;
    top: 736px;
    width: 1070px;
    margin: 0;
    font-size: 29px;
    line-height: 35px;
    font-weight: 400;
    color: var(--navy-text);
  }
  .cta-button {
    position: absolute;
    left: 443px;
    top: 898px;
    width: 314px;
    height: 84px;
    border-radius: 5px;
    background: var(--button-red);
    color: var(--white);
    font-weight: 700;
    font-size: 33px;
    line-height: 84px;
    text-align: center;
    text-decoration: none;
    letter-spacing: 0.5px;
  }
  .site-url {
    position: absolute;
    left: 790px;
    top: 926px;
    margin: 0;
    font-size: 20px;
    line-height: 28px;
    letter-spacing: 3.5px;
    color: var(--white);
  }
</style>
</head>
<body>
  <div class="banner">
    <svg class="banner-shapes" viewBox="0 0 1200 1001" aria-hidden="false">
      <defs>
        <linearGradient id="classroom-tones" x1="0" y1="0" x2="1" y2="1">
          <stop offset="0" stop-color="var(--photo-light)"/>
          <stop offset="0.35" stop-color="var(--photo-mid)"/>
          <stop offset="0.5" stop-color="var(--photo-teal)"/>
          <stop offset="0.75" stop-color="var(--photo-warm)"/>
          <stop offset="1" stop-color="var(--photo-light)"/>
        </linearGradient>
      </defs>
      <polygon class="photo-frame" points="0,106 1200,47 1200,620 0,660" fill="var(--white)"/>
      <polygon class="photo-area" points="0,114 1200,55 1200,612 0,652"
               fill="url(#classroom-tones)" role="img"
               aria-label="Photo: a smiling teacher with an open book speaking to students in a classroom"/>
      <polygon class="message-panel" points="0,642 1200,594 1200,812 0,868" fill="var(--white)"/>
    </svg>

    <p class="brand-name">LOGO</p>

    <h1 class="headline">SPEECH-LANGUAGE <span class="headline-accent">PATHOLOGIST SURVEY</span></h1>

    <p class="body-copy">Please take two minutes to complete a survey on the future of work patterns for Speech-Language Pathologists and enter a draw to win an Tabrix</p>

    <a class="cta-button" href="#">GET STARTED</a>

    <p class="site-url">www.yoururl.com</p>
  </div>
</body>
</html>
```